Visitenkarten-Design für Lichtfeder - Zeilen von Hand zu Hand
Zielgruppe
Ich schreibe Briefe an Menschen, die mehr über sich erfahren wollen, die sich berühren lassen wollen, die an sich arbeiten möchten, die sich entfalten wollen. Ich möchte nicht den Verstand sondern das Herz ansprechen, die Selbstheilung erfahren möchten, damit sie Impulse bekommen, um ein glücklicheres Leben zu führen, das ihnen mehr entspricht.
Ich sehe mich als Mensch, der andere Menschen in ihrem Leben unterstützen möchte.
Aufgabenstellung
Die Briefe schreibe ich in Segoe Print, goldene Schrift auf gelblichem Papier, evtl auch anderes Papier, wenn die goldene Schrift passt.
Die Visitenkarte sollte Freude, Freiheit und Anerkennung des Menschen an sich ausstrahlen. Farben evtl. Bordeaux, mit vielleicht Rosa. Sie sollte jedoch nicht kitschig wirken.
Schön wäre vielleicht etwas mit Blumen oder Ornamenten, jedoch nicht zu überladen.
Als Text soll drauf sein:
Das beigefügte Logo, dann:
Berühren - Bewegen - Begeistern

```html
<!DOCTYPE html>
<html lang="de">
<head>
<meta charset="utf-8">
<title>Lichtfeder – Visitenkarte</title>
<link href="https://fonts.googleapis.com/css2?family=Kaushan+Script&family=Mulish:wght@400;600;700&display=swap" rel="stylesheet">
<style>
  :root {
    --page: #faf7ee;
    --bordeaux: #520024;
    --gold: #c9a22d;
    --cream: #f5eedb;
    --quote: #7a2d4a;
    --white: #ffffff;
  }
  * { margin: 0; padding: 0; box-sizing: border-box; }
  html, body {
    width: 1184px; height: 1200px; overflow: hidden;
    background: var(--page);
    font-family: "Mulish", sans-serif;
  }
  .canvas { position: relative; width: 1184px; height: 1200px; }

  .card {
    position: absolute;
    width: 463px; height: 715px;
    overflow: hidden;
  }
  .card--front { left: 153px; top: 62px; background: var(--bordeaux); }
  .card--back { left: 556px; top: 408px; background: var(--bordeaux); }

  .gold-band {
    position: absolute; left: 0; right: 0; bottom: 0;
    height: 21px; background: var(--gold);
  }

  .brand {
    position: absolute; left: 0; right: 0; top: 272px;
    display: flex; align-items: center; justify-content: center; gap: 14px;
    color: var(--white);
    font-family: "Mulish", sans-serif;
    font-weight: 600;
    font-size: 54px;
    letter-spacing: 1px;
  }
  .brand__dot {
    width: 14px; height: 14px; border-radius: 50%;
    background: var(--gold);
  }

  .tagline {
    position: absolute; left: 0; right: 0; top: 592px;
    text-align: center;
    color: var(--white);
    font-size: 24px; line-height: 37px;
    letter-spacing: 1.5px;
    text-transform: uppercase;
  }
  .website {
    position: absolute; left: 0; right: 0; top: 690px;
    text-align: center;
    color: var(--gold);
    font-size: 23px; font-weight: 700;
    letter-spacing: 0.8px;
  }

  .back__top {
    position: absolute; left: 0; top: 0; width: 100%; height: 413px;
    background: var(--cream);
  }
  .back__divider {
    position: absolute; left: 0; top: 413px; width: 100%; height: 7px;
    background: var(--gold);
  }
  .accent-line {
    position: absolute; left: 59px; top: 78px;
    width: 287px; height: 6px; background: var(--gold);
  }
  .accent-dot {
    position: absolute; left: 378px; top: 66px;
    width: 28px; height: 28px; border-radius: 50%;
    border: 4px solid var(--bordeaux);
  }
  .motto {
    position: absolute; right: 40px; top: 140px;
    text-align: right;
    color: var(--quote);
    font-family: "Kaushan Script", cursive;
    font-size: 31px; line-height: 47px;
  }
  .contact {
    position: absolute; left: 43px; top: 558px;
    color: var(--white);
    font-size: 24px; line-height: 36px;
    letter-spacing: 0.4px;
  }
  .contact__name { font-weight: 700; }
</style>
</head>
<body>
<main class="canvas">
  <section class="card card--front" aria-label="Vorderseite">
    <div class="brand"><span class="brand__name">Lichtfeder</span><span class="brand__dot"></span></div>
    <p class="tagline">Zeilen von<br>Hand zu Hand</p>
    <p class="website">www.marlenehofstetter.de</p>
    <div class="gold-band"></div>
  </section>

  <section class="card card--back" aria-label="Rückseite">
    <div class="back__top">
      <div class="accent-line"></div>
      <div class="accent-dot"></div>
      <p class="motto">Mein Anliegen ist es,<br>Sie zu begeistern,<br>damit Sie Begeisterung<br>über Sich selbst<br>erkennen und erfahren.</p>
    </div>
    <div class="back__divider"></div>
    <address class="contact" style="font-style:normal">
      <div class="contact__name">Marlene Hofstetter</div>
      <div>lichtfeder@postwerk.de</div>
      <div>+49 160 55 214 907</div>
    </address>
    <div class="gold-band"></div>
  </section>
</main>
</body>
</html>
```